Oil and Gas Exploration and Production company needs a business card design

We need a business card design using our logo and colors in the logo. We want a mainstream design.

```html
<!DOCTYPE html>
<html lang="en">
<head>
<meta charset="utf-8">
<title>Ardent Oil &amp; Gas — Business Card</title>
<link href="https://fonts.googleapis.com/css2?family=Roboto+Slab:wght@400;700;800&family=Roboto:wght@400&display=swap" rel="stylesheet">
<style>
  :root {
    --gold: #c5952e;
    --ink: #141414;
    --dark-drop: #2a2321;
    --paper: #f4f4f2;
    --text-grey: #444444;
    --backdrop: #e6e4e0;
    --white: #ffffff;
  }
  * { margin: 0; padding: 0; box-sizing: border-box; }
  html, body { width: 1200px; height: 960px; overflow: hidden; }
  body { background: var(--backdrop); position: relative; font-family: "Roboto", Arial, sans-serif; }

  .card { position: absolute; box-shadow: 0 2px 6px rgba(0,0,0,0.25); }

  .card-front { left: 314px; top: 113px; width: 629px; height: 343px; background: var(--paper); }
  .name-band {
    position: absolute; left: 0; top: 54px; width: 340px; height: 60px;
    background: var(--gold); padding: 10px 0 0 38px; color: var(--white);
    font-family: "Roboto Slab", Georgia, serif;
  }
  .person-name { font-size: 20px; font-weight: 700; letter-spacing: 0.5px; line-height: 24px; }
  .person-title { font-size: 14px; font-weight: 400; line-height: 18px; }

  .brand-mark {
    position: absolute; left: 323px; top: 62px; width: 44px; height: 44px;
    border-radius: 50%; background: var(--ink);
  }
  .brand-name {
    position: absolute; right: 65px; top: 40px; text-align: right;
    font-family: "Roboto Slab", Georgia, serif; font-weight: 800; color: var(--ink);
  }
  .brand-name .line-main { display: block; font-size: 58px; line-height: 62px; letter-spacing: -1px; }
  .brand-name .line-sub { display: block; font-size: 23px; line-height: 28px; letter-spacing: 3px; }

  .contact-list { position: absolute; left: 38px; top: 234px; list-style: none; font-size: 14px; color: var(--text-grey); }
  .contact-list li { display: flex; align-items: center; height: 19px; }
  .contact-list svg { width: 14px; height: 14px; margin-right: 9px; fill: var(--ink); }

  .address { position: absolute; right: 65px; top: 256px; text-align: right; font-size: 14px; line-height: 18px; color: var(--text-grey); font-style: normal; }

  .card-back { left: 311px; top: 472px; width: 600px; height: 342px; background: var(--gold); }
  .back-lockup {
    position: absolute; left: 0; top: 120px; width: 100%;
    display: flex; justify-content: center; align-items: center; gap: 18px;
  }
  .back-mark { width: 56px; height: 56px; border-radius: 50%; background: var(--dark-drop); }
  .back-name { font-family: "Roboto Slab", Georgia, serif; font-weight: 800; font-size: 40px; color: var(--dark-drop); letter-spacing: 1px; }
  .back-web { position: absolute; left: 0; top: 287px; width: 100%; text-align: center; color: var(--white); font-size: 14px; letter-spacing: 5.5px; }
</style>
</head>
<body>
  <section class="card card-front">
    <div class="name-band">
      <div class="person-name">DANIEL REYES</div>
      <div class="person-title">CEO/FOUNDER</div>
    </div>
    <div class="brand-mark"></div>
    <div class="brand-name">
      <span class="line-main">Ardent</span>
      <span class="line-sub">OIL &amp; GAS</span>
    </div>

    <ul class="contact-list">
      <li><svg viewBox="0 0 16 16"><path d="M3.5 1 6 1.6 7 5 5.4 6.4c.8 1.7 2.4 3.3 4.2 4.2L11 9l3.4 1 .6 2.5c-.3 1.3-1.4 2.3-2.8 2.3C6.3 14.8 1.2 9.7 1.2 3.8 1.2 2.4 2.2 1.3 3.5 1z"/></svg>512 774 3016</li>
      <li><svg viewBox="0 0 16 16"><path d="M4.5 0h7A1.5 1.5 0 0 1 13 1.5v13a1.5 1.5 0 0 1-1.5 1.5h-7A1.5 1.5 0 0 1 3 14.5v-13A1.5 1.5 0 0 1 4.5 0zM5 2v10h6V2zm3 11a1 1 0 1 0 0 2 1 1 0 0 0 0-2z"/></svg>907 215 4830</li>
      <li><svg viewBox="0 0 16 16"><path d="M4 1h8v4H4zM1 6h14v7h-2v-2H3v2H1zm3 6h8v3H4z"/></svg>318 602 7459</li>
      <li><svg viewBox="0 0 16 16"><path d="M1 3h14v1.2L8 8.6 1 4.2zm0 2.6 7 4.4 7-4.4V13H1z"/></svg>info@ardentoilgas.com</li>
    </ul>

    <address class="address">
      1420 Birchwood Road<br>
      Juneau, Alaska 99801<br>
      www.ardentoilgas.com
    </address>
  </section>

  <section class="card card-back">
    <div class="back-lockup">
      <div class="back-mark"></div>
      <div class="back-name">Ardent Oil &amp; Gas</div>
    </div>
    <div class="back-web">www.ardentoilgas.com</div>
  </section>
</body>
</html>
```